Re-design Vodka Label

3 main outcomes:

1. The animal needs to look more like an actual Sable Crest (photo attached)
2. The text, spacing etc should fit the bottle well (see bottle size specs and photo attached)
3. Show me 1) a design with front label/logo only and 2) front and back label

Current artwork attached

```html
<!DOCTYPE html>
<html lang="en">
<head>
<meta charset="utf-8">
<title>Sable Crest Vodka – Front Label</title>
<link rel="stylesheet" href="https://fonts.googleapis.com/css2?family=Oswald:wght@300;400;700&display=swap">
<style>
  :root {
    --backdrop: #b5b2b1;
    --label-white: #ffffff;
    --ink: #2d2d2d;
    --accent-red: #c0202a;
    --seal-red: #c8151d;
    --seal-dark: #9a0f15;
    --art-dark: #3a2418;
    --art-mid: #6a4128;
  }
  * { margin: 0; padding: 0; box-sizing: border-box; }
  html, body {
    width: 1200px;
    height: 906px;
    overflow: hidden;
    background: var(--backdrop);
  }
  .canvas {
    position: relative;
    width: 1200px;
    height: 906px;
    display: flex;
    align-items: center;
    justify-content: center;
  }
  .label { display: block; }
  .label-body { fill: var(--label-white); }
  .label-frame { fill: none; stroke: var(--accent-red); stroke-width: 2; }
  .rule { stroke: var(--ink); stroke-width: 1.4; }
  .brand-name {
    font-family: "Oswald", sans-serif;
    font-weight: 700;
    font-size: 66px;
    fill: var(--ink);
    letter-spacing: 0.5px;
  }
  .product-type {
    font-family: "Oswald", sans-serif;
    font-weight: 400;
    font-size: 66px;
    fill: var(--accent-red);
  }
  .tagline {
    font-family: "Oswald", sans-serif;
    font-weight: 400;
    font-size: 17px;
    fill: var(--ink);
  }
  .spec {
    font-family: "Oswald", sans-serif;
    font-weight: 300;
    font-size: 16px;
    fill: var(--ink);
  }
  .seal { fill: var(--seal-red); stroke: var(--seal-dark); stroke-width: 3; }
</style>
</head>
<body>
<main class="canvas">
  <svg class="label" width="426" height="830" viewBox="0 0 426 830" xmlns="http://www.w3.org/2000/svg">
    <defs>
      <linearGradient id="artTone" x1="0" y1="0" x2="0" y2="1">
        <stop offset="0" stop-color="var(--art-dark)"/>
        <stop offset="0.55" stop-color="var(--art-mid)"/>
        <stop offset="1" stop-color="var(--art-dark)"/>
      </linearGradient>
    </defs>

    <path class="label-body" d="M0 828 V321 A213 213 0 0 1 426 321 V828 Z"/>
    <path class="label-frame" d="M15 813 V327 A195 195 0 0 1 411 327 V813 Z"/>

    <rect class="mascot-art" role="img" aria-label="Illustrated head of a dark brown antelope with long ridged horns, facing forward"
          x="79" y="3" width="275" height="493" rx="40" fill="url(#artTone)"/>

    <text class="brand-name" x="218" y="563" text-anchor="middle" textLength="344" lengthAdjust="spacingAndGlyphs">SABLE CREST</text>
    <line class="rule" x1="78" y1="574" x2="358" y2="574"/>
    <text class="product-type" x="218" y="638" text-anchor="middle">Vodka</text>

    <text class="tagline" x="218" y="691" text-anchor="middle">METICULOUSLY CRAFTED,</text>
    <text class="tagline" x="218" y="712" text-anchor="middle" textLength="249" lengthAdjust="spacingAndGlyphs">DISTILLED FROM ZAMBIA’S FINEST GRAINS</text>

    <line class="rule" x1="49" y1="754" x2="138" y2="754"/>
    <line class="rule" x1="49" y1="799" x2="138" y2="799"/>
    <text class="spec" x="93" y="783" text-anchor="middle">40% Alc. Vol</text>

    <circle class="seal" cx="218" cy="775" r="35"/>

    <line class="rule" x1="300" y1="754" x2="387" y2="754"/>
    <line class="rule" x1="300" y1="799" x2="387" y2="799"/>
    <text class="spec" x="343" y="783" text-anchor="middle">750ml</text>
  </svg>
</main>
</body>
</html>
```